Anzeigengestaltung für Beratungsunternehmen
Zielgruppe
Firmenname: WERKSCHUTZPLAN.ORG | Beratung in den Bereichen: Arbeitssicherheit, Brandschutz und Gefahrgut | Zielgruppe: Unternehmen, die Beratung zu obigen Themen suchen | Meine Qualifikationen: Fachkraft für Arbeitssicherheit, Gefahrgut- und Brandschutzbeauftragter, Sachkundiger nach ChemVerbotsV, Ausbilder für Flurförderzeuge, Krane, Hubarbeitsbühnen und Brandschutzhelfer (auch die Ausbilder-Themen könnten erscheinen/hervorgehoben werden - ich biete dafür Kurse an)
Aufgabenstellung
Es soll für Werbung in Zeitschriften und auch für Werbebanner geeignet sein. Vielleicht in 16:9?! Mal hochkant, mal quer.

```html
<!DOCTYPE html>
<html lang="de">
<head>
<meta charset="utf-8">
<title>WERKSCHUTZPLAN.ORG – Anzeige</title>
<link rel="stylesheet" href="https://fonts.googleapis.com/css2?family=Jost:wght@700&family=Montserrat:wght@400;600;700&family=Kalam:wght@700&display=swap">
<style>
  :root {
    --red: #ab1118;
    --ink: #0d0d0d;
    --white: #ffffff;
    --mist: #e9e9e9;
    --grey: #bfbfbf;
  }
  * { box-sizing: border-box; margin: 0; padding: 0; }
  html, body { width: 1200px; height: 2400px; overflow: hidden; background: var(--white); }
  .ad { position: relative; width: 1200px; height: 2400px; overflow: hidden; background: var(--white); font-family: "Montserrat", sans-serif; color: var(--ink); }

  .headline { position: absolute; left: 0; top: 0; width: 100%; font-family: "Jost", sans-serif; font-weight: 700; font-size: 108px; line-height: 1; }
  .headline .line { position: absolute; white-space: nowrap; }
  .headline .plain { color: var(--ink); }
  .headline .mark { position: absolute; background: var(--red); color: var(--white); padding-left: 10px; white-space: nowrap; }
  .line-1 { left: 118px; top: 118px; }
  .mark-1 { left: 110px; top: 238px; width: 960px; height: 113px; padding-top: 4px; }
  .comma { left: 112px; top: 386px; }
  .mark-2 { left: 164px; top: 382px; width: 737px; height: 115px; padding-top: 4px; padding-left: 18px; }
  .und { left: 118px; top: 528px; }
  .mark-3 { left: 344px; top: 523px; width: 628px; height: 114px; padding-top: 6px; padding-left: 16px; }

  .qualifications { position: absolute; left: 140px; top: 730px; width: 1020px; list-style: none; }
  .qualifications li { position: relative; padding-left: 86px; font-size: 38px; line-height: 1.36; letter-spacing: 0.3px; margin-bottom: 18px; }
  .qualifications svg { position: absolute; left: 0; top: 2px; width: 54px; height: 58px; }
  .qualifications strong { font-weight: 700; }

  .scene-backdrop { position: absolute; left: 0; top: 1100px; width: 1200px; height: 900px; background: linear-gradient(180deg, #ffffff 0%, #e4e4e4 25%, #d6d6d6 60%, #ececec 100%); }
  .photo { position: absolute; background: var(--white); padding: 9px; box-shadow: 0 6px 18px rgba(0,0,0,.25); }
  .photo .fill { width: 100%; height: 100%; }
  .photo-safety { left: 78px; top: 1177px; width: 495px; height: 368px; transform: rotate(-2deg); }
  .photo-safety .fill { background: linear-gradient(135deg, #5a5c60, #2e3138 60%, #c9a23a); }
  .photo-hazard { left: 612px; top: 1097px; width: 500px; height: 342px; transform: rotate(-1.5deg); }
  .photo-hazard .fill { background: linear-gradient(120deg, #e2d9a8 0%, #8d9096 45%, #c62b2b 62%, #dfdfdf 100%); }
  .photo-extinguisher { left: 705px; top: 1480px; width: 418px; height: 345px; transform: rotate(-1deg); }
  .photo-extinguisher .fill { background: linear-gradient(160deg, #2f4f9b 0%, #3a3d45 40%, #c62128 75%, #2a2a2a 100%); }
  .portrait { position: absolute; left: 294px; top: 1380px; width: 631px; height: 560px; background: linear-gradient(180deg, #d9d9d9 0%, #b78d72 30%, #e6e8ee 55%, #1f2742 75%, #151b30 100%); border-radius: 46% 46% 0 0 / 30% 30% 0 0; }

  .call-out { position: absolute; left: 96px; top: 1600px; font-family: "Kalam", cursive; font-weight: 700; line-height: 1; transform: rotate(-4deg); z-index: 3; }
  .call-out .now { display: block; font-size: 74px; color: var(--ink); }
  .call-out .call { display: block; font-size: 82px; color: var(--red); margin-left: 6px; margin-top: -6px; }

  .contact-band { position: absolute; left: 0; top: 0; width: 1200px; height: 2400px; z-index: 2; }
  .person-name { position: absolute; left: 118px; top: 1972px; font-family: "Montserrat", sans-serif; font-weight: 700; font-size: 66px; line-height: 1; white-space: nowrap; transform: rotate(-3deg); transform-origin: left bottom; z-index: 5; }
  .person-name .last { color: var(--red); }

  .contact-list { position: absolute; left: 104px; top: 2128px; list-style: none; color: var(--white); z-index: 5; }
  .contact-list li { display: flex; align-items: center; font-size: 42px; height: 59px; letter-spacing: 0.3px; white-space: nowrap; }
  .contact-list svg { width: 36px; height: 36px; margin-right: 32px; flex: none; }

  .brand-seal { position: absolute; left: 734px; top: 1913px; width: 396px; height: 396px; border-radius: 50%; background: var(--white); border: 14px solid var(--red); display: flex; align-items: center; justify-content: center; z-index: 6; }
  .brand-seal span { font-family: "Montserrat", sans-serif; font-weight: 700; font-size: 24px; color: var(--red); white-space: nowrap; }
</style>
</head>
<body>
<main class="ad">

  <h1 class="headline">
    <span class="line line-1 plain">Ihr Partner für</span>
    <span class="mark mark-1">Arbeitssicherheit</span>
    <span class="line comma plain">,</span>
    <span class="mark mark-2">Brandschutz</span>
    <span class="line und plain">und</span>
    <span class="mark mark-3">Gefahrgut</span>
  </h1>

  <ul class="qualifications">
    <li>
      <svg viewBox="0 0 54 58" aria-hidden="true"><path d="M27 3 L50 10 V28 C50 42 40 51 27 55 C14 51 4 42 4 28 V10 Z" fill="none" stroke="#ab1118" stroke-width="5"/><path d="M15 28 L25 39 L45 9" fill="none" stroke="#0d0d0d" stroke-width="6" stroke-linecap="round" stroke-linejoin="round"/></svg>
      Fachkraft für Arbeitssicherheit, Gefahrgut-<br>und Brandschutzbeauftragter
    </li>
    <li>
      <svg viewBox="0 0 54 58" aria-hidden="true"><path d="M27 3 L50 10 V28 C50 42 40 51 27 55 C14 51 4 42 4 28 V10 Z" fill="none" stroke="#ab1118" stroke-width="5"/><path d="M15 28 L25 39 L45 9" fill="none" stroke="#0d0d0d" stroke-width="6" stroke-linecap="round" stroke-linejoin="round"/></svg>
      Sachkundiger nach <strong>ChemVerbotsV</strong>
    </li>
    <li>
      <svg viewBox="0 0 54 58" aria-hidden="true"><path d="M27 3 L50 10 V28 C50 42 40 51 27 55 C14 51 4 42 4 28 V10 Z" fill="none" stroke="#ab1118" stroke-width="5"/><path d="M15 28 L25 39 L45 9" fill="none" stroke="#0d0d0d" stroke-width="6" stroke-linecap="round" stroke-linejoin="round"/></svg>
      Ausbilder für Flurförderzeuge, Krane,<br>Hubarbeitsbühnen und Brand-<br>schutzhelfer
    </li>
  </ul>

  <div class="scene-backdrop" role="img" aria-label="Blasse Industriehalle mit Maschinen im Hintergrund"></div>

  <figure class="photo photo-safety"><div class="fill" role="img" aria-label="Tafel mit der Aufschrift Safe Work Practices und gelbem Schutzhelm"></div></figure>
  <figure class="photo photo-hazard"><div class="fill" role="img" aria-label="Schutzhandschuh vor Gefahrgutkennzeichen"></div></figure>
  <figure class="photo photo-extinguisher"><div class="fill" role="img" aria-label="Techniker prüft rote Feuerlöscher"></div></figure>

  <div class="portrait" role="img" aria-label="Porträt des Beraters im dunklen Anzug"></div>

  <p class="call-out"><span class="now">Jetzt</span><span class="call">Anrufen!</span></p>

  <svg class="contact-band" viewBox="0 0 1200 2400" aria-hidden="true">
    <polygon points="0,1940 1200,1940 1200,2400 0,2400" fill="#ffffff"/>
    <polygon points="0,2086 1200,2027 1200,2400 0,2400" fill="#ab1118"/>
  </svg>

  <p class="person-name">Tobias <span class="last">Krämer</span></p>

  <ul class="contact-list">
    <li>
      <svg viewBox="0 0 24 24"><path d="M6.6 10.8a15.2 15.2 0 0 0 6.6 6.6l2.2-2.2c.3-.3.7-.4 1-.2 1.1.4 2.3.6 3.6.6.6 0 1 .4 1 1V20c0 .6-.4 1-1 1C10.6 21 3 13.4 3 4c0-.6.4-1 1-1h3.5c.6 0 1 .4 1 1 0 1.3.2 2.5.6 3.6.1.3 0 .7-.2 1z" fill="#fff"/></svg>
      +49 151 20 48 36 17
    </li>
    <li>
      <svg viewBox="0 0 24 24"><rect x="2" y="5" width="20" height="14" rx="1.5" fill="#fff"/><path d="M2.5 6 L12 13 L21.5 6" fill="none" stroke="#ab1118" stroke-width="1.8"/></svg>
      info@werkschutzplan.org
    </li>
    <li>
      <svg viewBox="0 0 24 24"><circle cx="12" cy="12" r="9.5" fill="none" stroke="#fff" stroke-width="2"/><ellipse cx="12" cy="12" rx="4" ry="9.5" fill="none" stroke="#fff" stroke-width="2"/><path d="M2.5 12 H21.5 M4 7.5 H20 M4 16.5 H20" stroke="#fff" stroke-width="2"/></svg>
      www.werkschutzplan.org
    </li>
  </ul>

  <div class="brand-seal"><span>WERKSCHUTZPLAN.ORG</span></div>

</main>
</body>
</html>
```